Printing technique figures for thesis

The following schematics of different printing techniques are to be included in my doctoral thesis in pharmaceutics and it is therefore of importance that the techniques are described accurately. See the attached file for more detailed information.

Target Market(s)

Science, pharmaceutical

Font styles to use
Other font styles liked:
• Cambria

Requirements
Must have
• Accurate figure representing the printing method
Nice to have
• 3D figures

```html
<!DOCTYPE html>
<html lang="en">
<head>
<meta charset="utf-8">
<title>Printing Techniques Overview</title>
<link rel="stylesheet" href="https://fonts.googleapis.com/css2?family=Open+Sans:wght@800&family=Source+Sans+3:wght@400&display=swap">
<style>
  :root {
    --header-bg: #f2f2f2;
    --stage-bg: #2e2e2e;
    --title-ink: #2e2e2e;
    --node-light: #9396c8;
    --node-mid: #6e6f95;
    --node-deep: #474e6e;
    --node-grey: #818181;
    --hub-fill: #ffffff;
    --hub-ring: #3b2f6b;
    --hub-ink: #555555;
    --label-light: #ffffff;
    --label-dark: #1a1770;
  }
  html, body { margin: 0; padding: 0; overflow: hidden; }
  body { width: 1200px; height: 739px; background: var(--stage-bg); }
  .chart { display: block; width: 1200px; height: 739px; }
  .header-band { fill: var(--header-bg); }
  .stage { fill: var(--stage-bg); }
  .chart-title { font-family: "Source Sans 3", sans-serif; font-size: 72px; fill: var(--title-ink); }
  .node text { font-family: "Source Sans 3", sans-serif; fill: var(--label-light); text-anchor: middle; }
  .node--light circle { fill: var(--node-light); }
  .node--mid circle { fill: var(--node-mid); }
  .node--deep circle { fill: var(--node-deep); }
  .node--grey circle { fill: var(--node-grey); }
  .node--dark-label text { fill: var(--label-dark); }
  .hub circle { fill: var(--hub-fill); stroke: var(--hub-ring); stroke-width: 2; }
  .hub text { fill: var(--hub-ink); }
  .hub .hub-mark { font-family: "Open Sans", sans-serif; font-weight: 800; font-size: 64px; }
  .size-l { font-size: 38px; }
  .size-m { font-size: 32px; }
  .size-s { font-size: 30px; }
  .size-xs { font-size: 26px; }
</style>
</head>
<body>
<svg class="chart" viewBox="0 0 2455 1512" xmlns="http://www.w3.org/2000/svg" role="img" aria-label="Printing techniques overview: 2D, 3D and 4D printing methods">
  <rect class="stage" x="0" y="0" width="2455" height="1512"/>
  <rect class="header-band" x="12" y="0" width="2443" height="248"/>
  <text class="chart-title" x="1234" y="146" text-anchor="middle">Printing Techniques Overview</text>

  <!-- 2D group -->
  <g class="node node--mid"><circle cx="481" cy="440" r="80"/><text class="size-xs" x="481" y="434">Flexographic</text><text class="size-xs" x="481" y="462">printing</text></g>
  <g class="node node--mid"><circle cx="709" cy="488" r="80"/><text class="size-xs" x="709" y="483">Stencil</text><text class="size-xs" x="709" y="510">printing</text></g>
  <g class="node node--light"><circle cx="563" cy="580" r="105"/><text class="size-m" x="563" y="568">Contact</text><text class="size-m" x="563" y="602">Methods</text></g>
  <g class="node node--mid"><circle cx="208" cy="720" r="80"/><text class="size-xs" x="208" y="731">Continuous</text></g>
  <g class="node node--light"><circle cx="344" cy="807" r="105"/><text class="size-m" x="344" y="801">Inkjet</text><text class="size-m" x="344" y="835">printing</text></g>
  <g class="node node--light"><circle cx="775" cy="794" r="105"/><text class="size-m" x="775" y="787">Non-contact</text><text class="size-m" x="775" y="820">Methods</text></g>
  <g class="node node--deep"><circle cx="187" cy="960" r="66"/></g>
  <g class="node node--mid"><circle cx="321" cy="977" r="80"/><text class="size-xs" x="321" y="961">Drop</text><text class="size-xs" x="321" y="988">on</text><text class="size-xs" x="321" y="1014">demand</text></g>
  <g class="node node--deep"><text class="size-xs" x="187" y="970">Electrostatic</text></g>
  <g class="node node--deep"><circle cx="462" cy="993" r="66"/><text class="size-xs" x="462" y="994">Solenoid</text><text class="size-xs" x="462" y="1021">valve</text></g>
  <g class="node node--deep"><circle cx="241" cy="1090" r="66"/><text class="size-xs" x="241" y="1101">Acoustic</text></g>
  <g class="node node--grey"><circle cx="479" cy="1175" r="60"/><text class="size-xs" x="479" y="1183" style="font-size:22px">Thermal</text></g>
  <g class="node node--deep"><circle cx="379" cy="1109" r="66"/><text class="size-xs" x="379" y="1103">Inkjet</text><text class="size-xs" x="379" y="1131">printing</text></g>
  <g class="node node--grey node--dark-label"><circle cx="367" cy="1222" r="60"/><text x="365" y="1229" style="font-size:22px">Piezoelectric</text></g>
  <g class="node hub"><circle cx="564" cy="795" r="126"/><text class="hub-mark" x="566" y="818">2D</text></g>

  <!-- 3D group -->
  <g class="node node--mid"><circle cx="1247" cy="449" r="72"/><text class="size-xs" x="1247" y="444">Drop on solid</text><text class="size-xs" x="1247" y="471">deposition</text></g>
  <g class="node node--light"><circle cx="1232" cy="612" r="105"/><text class="size-m" x="1232" y="581">Powder</text><text class="size-m" x="1232" y="615">solidification</text><text class="size-m" x="1232" y="648">3D printing</text></g>
  <g class="node node--mid"><circle cx="1377" cy="697" r="72"/><text class="size-xs" x="1377" y="698" style="font-size:24px">Selective laser</text><text class="size-xs" x="1377" y="725" style="font-size:24px">sintering</text></g>
  <g class="node node--light"><circle cx="1097" cy="1006" r="105"/><text class="size-m" x="1097" y="1007">Extrusion-based</text><text class="size-m" x="1097" y="1040">3D printing</text></g>
  <g class="node node--mid node--dark-label"><circle cx="985" cy="1138" r="72"/><text class="size-xs" x="985" y="1117">Fused</text><text class="size-xs" x="985" y="1144">deposition</text><text class="size-xs" x="985" y="1171">modeling</text></g>
  <g class="node node--mid node--dark-label"><circle cx="1209" cy="1138" r="72"/><text class="size-xs" x="1209" y="1119">Semisolid</text><text class="size-xs" x="1209" y="1146">extrusion 3D</text><text class="size-xs" x="1209" y="1173">printing</text></g>
  <g class="node hub"><circle cx="1133" cy="800" r="126"/><text class="hub-mark" x="1131" y="823">3D</text></g>

  <!-- Liquid solidification group -->
  <g class="node node--light"><circle cx="1742" cy="618" r="105"/><text class="size-m" x="1742" y="610">Drop-on-drop</text><text class="size-m" x="1742" y="643">deposition</text></g>
  <g class="node node--light"><circle cx="1607" cy="1013" r="120"/><text class="size-m" x="1607" y="1023">Stereolithography</text></g>
  <g class="node hub"><circle cx="1643" cy="806" r="126"/><text class="size-s" x="1640" y="744">Liquid</text><text class="size-s" x="1643" y="782">solidification</text><text class="hub-mark" x="1639" y="842">3D</text><text class="size-s" x="1643" y="876">printing</text></g>

  <!-- 4D group -->
  <g class="node node--light"><circle cx="2042" cy="1020" r="105"/><text class="size-m" x="2042" y="1002">3D printing</text><text class="size-m" x="2042" y="1037">+</text><text class="size-m" x="2042" y="1068">time</text></g>
  <g class="node hub"><circle cx="2079" cy="815" r="126"/><text class="hub-mark" x="2079" y="838">4D</text></g>
</svg>
</body>
</html>
```